Driving-coach/trainer who wants to inform about the offer and how I can help people to drive more re

I need a flyer that informs potential customers about my offer.

DL size 210 mm x 99 mm, vertical!

I'm a trainer/coach who helps people to drive a car more relaxed, without fear and more confident.

It's a one to one training. I do train people in their own car. It gets people their freedom back to go where and when they like to go by own car...

Target Market(s)

People (man an woman) who are afraid of driving a car, or are very stressed while driving....

Industry/Entity Type

Life Coaching

Font styles to use
Sans Serif

Colors
acd136

Requirements
Must have
• Page 1:
• -my offer (see text-pdf)
• -three fotos (see attached files "Pixmarra") of people who are satisfied with my offer
• Page 2:
• -advantages in the work with me.
• -contact information
• -and a picture of me (see attached file) next to the contact information or the advantages of my work
• -my logo (see attached file) on Page 1 + 2
• -i like a "clear" and structured layout. "Less is more"

```html
<!DOCTYPE html>
<html lang="de">
<head>
<meta charset="utf-8">
<title>Fahrangst-Coaching Flyer</title>
<link rel="stylesheet" href="https://fonts.googleapis.com/css2?family=Open+Sans:wght@300;400;600&family=Ubuntu:wght@300;400;500;700&display=swap">
<style>
  :root{
    --green:#acd136;
    --green-dark:#8fb21f;
    --ink:#2b2b2b;
    --paper:#f3f3f1;
    --facet:#e4e4e2;
    --stage:#e9e9e9;
  }
  *{box-sizing:border-box;margin:0;padding:0}
  html,body{width:1200px;height:1200px;overflow:hidden;background:var(--stage)}
  body{font-family:"Open Sans",sans-serif;color:var(--ink);position:relative}
  .flyer{position:absolute;top:91px;width:480px;height:1018px;background:var(--paper);overflow:hidden;box-shadow:0 4px 18px rgba(0,0,0,.18)}
  .flyer--front{left:90px}
  .flyer--back{left:630px}
  .photo{position:absolute;left:0;top:0;width:480px}
  .flyer--front .photo{height:420px;background:linear-gradient(135deg,#8a8f93 0%,#c9b79c 45%,#e0d2bd 70%,#9aa0a3 100%)}
  .flyer--back .photo{height:370px;background:linear-gradient(135deg,#cfd6d8 0%,#e8c8a8 45%,#f0e2d0 65%,#8e979b 100%)}
  .shapes{position:absolute;left:0;top:0}
  .headline{position:absolute;font-family:"Open Sans",sans-serif;font-weight:300;font-size:27px;line-height:1}
  .headline span{display:table;padding:3px 7px 4px;margin-bottom:3px}
  .headline--green span{background:var(--green);color:#fff}
  .headline--dark span{background:var(--ink);color:#fff}
  .badge{position:absolute;width:104px;height:104px;border-radius:50%;background:var(--ink);border:6px solid var(--green);color:var(--green);font-family:"Ubuntu",sans-serif;font-weight:700;font-size:13px;line-height:1.05;text-align:center;display:flex;align-items:center;justify-content:center}
  .green{color:var(--green-dark)}
  .section-title{position:absolute;font-family:"Ubuntu",sans-serif;font-weight:700;color:var(--green)}
  .questions{position:absolute;left:50px;top:425px;list-style:none;font-family:"Ubuntu",sans-serif;font-weight:500;font-size:17px}
  .questions li{margin-bottom:12px}
  .questions li::before{content:"»";color:var(--green);font-weight:700;margin-right:12px}
  .banner{position:absolute;left:40px;top:540px;width:375px;height:48px;background:var(--green);color:#fff;font-family:"Ubuntu",sans-serif;font-weight:700;font-size:20px;display:flex;align-items:center;padding-left:16px;box-shadow:5px 5px 0 var(--green-dark)}
  .banner::before{content:"";width:13px;height:13px;background:#fff;margin-right:14px}
  .lead{position:absolute;left:80px;top:608px;font-size:19px;line-height:1.2}
  .checks{position:absolute;list-style:none;font-size:10.5px;line-height:1.3}
  .checks li{position:relative;padding-left:30px}
  .checks li svg{position:absolute;left:0;top:1px}
  .flyer--front .checks{left:55px;top:670px;width:410px}
  .flyer--front .checks li{margin-bottom:11px}
  .flyer--back .checks{left:45px;top:590px;width:400px;font-size:11px;line-height:1.35}
  .flyer--back .checks li{margin-bottom:14px}
  .cheer{position:absolute;left:285px;top:850px;width:150px;text-align:center;font-family:"Ubuntu",sans-serif;font-weight:700;font-size:18px;line-height:1;color:var(--green)}
  .signature{position:absolute;left:45px;top:958px;font-family:"Ubuntu",sans-serif;color:var(--green-dark)}
  .signature .name{font-size:20px;letter-spacing:2px;font-weight:400;line-height:1.1}
  .signature .role{font-size:14px;letter-spacing:1.5px;font-weight:300;line-height:1.2}
  .steps{position:absolute;left:20px;top:395px;display:flex;gap:34px}
  .step{position:relative;width:112px;height:112px;border-radius:50%;background:var(--ink);border:6px solid var(--green);color:var(--green);font-family:"Ubuntu",sans-serif;font-weight:700;text-align:center;display:flex;align-items:center;justify-content:center;line-height:1}
  .step .num{position:absolute;left:-16px;top:-16px;width:44px;height:44px;border-radius:50%;background:var(--ink);border:4px solid #fff;color:#fff;font-size:24px;display:flex;align-items:center;justify-content:center}
  .contact-name{position:absolute;left:45px;top:830px;font-family:"Ubuntu",sans-serif;font-weight:700;font-size:20px}
  .contact-more{position:absolute;left:45px;top:857px;font-family:"Ubuntu",sans-serif;font-weight:500;font-size:12px;color:var(--green-dark)}
  .contact-web{position:absolute;left:45px;top:880px;font-family:"Ubuntu",sans-serif;font-weight:700;font-size:12px;display:flex;align-items:center;gap:8px}
  .coach-photo{position:absolute;left:330px;top:805px;width:150px;height:213px;background:linear-gradient(180deg,#c9a58c 0%,#e9e6e2 35%,#ffffff 100%);border-radius:70px 70px 0 0}
  .call-label{position:absolute;left:35px;top:962px;font-family:"Ubuntu",sans-serif;font-weight:700;font-size:12px;color:var(--green-dark)}
  .call-number{position:absolute;left:35px;top:982px;font-family:"Ubuntu",sans-serif;font-weight:700;font-size:21px;color:var(--green);display:flex;align-items:center;gap:8px}
</style>
</head>
<body>

<section class="flyer flyer--front">
  <div class="photo" role="img" aria-label="Foto: zufriedene Fahrerin im Cabrio, lächelnd am Steuer"></div>
  <svg class="shapes" width="480" height="1018" viewBox="0 0 480 1018" aria-hidden="true">
    <polygon points="0,420 170,275 300,330 480,175 480,1018 0,1018" fill="#f3f3f1"/>
    <polyline points="0,420 170,275 300,330 480,175" fill="none" stroke="#acd136" stroke-width="9"/>
    <polygon points="0,1018 0,975 110,935 210,915 350,960 480,890 480,1018" fill="#e4e4e2"/>
    <polygon points="110,935 210,915 180,990" fill="#ececea"/>
    <polygon points="350,960 480,890 480,970" fill="#dcdcda"/>
    <polyline points="0,975 110,935 210,915 350,960 480,890" fill="none" stroke="#acd136" stroke-width="6"/>
  </svg>
  <div class="headline headline--green" style="left:35px;top:70px">
    <span>FAHRANGST</span><span>ERFOLGREICH</span><span>ÜBERWINDEN!</span>
  </div>
  <div class="badge" style="left:365px;top:255px">ICH<br>HABS<br>GESCHAFF!!</div>
  <h2 class="section-title" style="left:100px;top:360px;font-size:30px">Wollen Sie</h2>
  <ul class="questions">
    <li>Fahrangst überwinden?</li>
    <li>Panikattacken beim Autofahren loswerden?</li>
    <li>Sicher und entspannt Autofahren?</li>
  </ul>
  <div class="banner">Dann sind Sie hier richtig!</div>
  <p class="lead">Kommt Ihnen eine dieser Situationen<br>bekannt vor?</p>
  <ul class="checks">
    <li><svg width="20" height="20" viewBox="0 0 20 20"><circle cx="10" cy="10" r="10" fill="#acd136"/><path d="M5 10.5l3.2 3L15 6.5" fill="none" stroke="#fff" stroke-width="2.4"/></svg>Autofahren erleben Sie unter hoher Anspannung und Stress. - Sie wünschen sich, Autofahren <span class="green">sicher und entspannt</span> zu erleben.</li>
    <li><svg width="20" height="20" viewBox="0 0 20 20"><circle cx="10" cy="10" r="10" fill="#acd136"/><path d="M5 10.5l3.2 3L15 6.5" fill="none" stroke="#fff" stroke-width="2.4"/></svg>Bestimmte Situationen (z.B. unbekannte Strecken, Autobahn, Baustellen, Stadtverkehr, Parken…) bereiten Ihnen großen Stress oder trauen Sie sich nicht zu. - Sie möchten diese Situationen <span class="green">gelassener und souveräner</span> meistern.</li>
    <li><svg width="20" height="20" viewBox="0 0 20 20"><circle cx="10" cy="10" r="10" fill="#acd136"/><path d="M5 10.5l3.2 3L15 6.5" fill="none" stroke="#fff" stroke-width="2.4"/></svg>Sie fühlen sich durch andere Verkehrsteilnehmer gestresst und unter Druck. Sie haben Angst auf unvorhergesehene Situationen nicht richtig reagieren zu können. - Sie möchten <span class="green">Autofahren entspannter und souveräner erleben.</span></li>
    <li><svg width="20" height="20" viewBox="0 0 20 20"><circle cx="10" cy="10" r="10" fill="#acd136"/><path d="M5 10.5l3.2 3L15 6.5" fill="none" stroke="#fff" stroke-width="2.4"/></svg>Angst oder Panikattacken begleiten Sie beim Autofahren. Vielleicht vermeiden Sie deshalb das Autofahren komplett. - Sie möchten <span class="green">angstfrei und entspannt Auto fahren.</span></li>
  </ul>
  <p class="cheer">Auch Sie<br>Können<br>es schaffen!!</p>
  <div class="signature">
    <p class="name">Karin Feldhaus</p>
    <p class="role">Fahrangst-Bewältigungs-Coach</p>
  </div>
</section>

<section class="flyer flyer--back">
  <div class="photo" role="img" aria-label="Foto: lachende junge Frau im Autofenster mit erhobenem Daumen"></div>
  <svg class="shapes" width="480" height="1018" viewBox="0 0 480 1018" aria-hidden="true">
    <polygon points="0,140 60,250 120,275 330,250 380,255 480,350 480,1018 0,1018" fill="#f3f3f1"/>
    <polyline points="0,140 60,250 120,275 330,250 380,255 480,350" fill="none" stroke="#acd136" stroke-width="9"/>
    <polygon points="0,1018 0,920 80,905 180,935 300,965 420,980 480,1018" fill="#e4e4e2"/>
    <polygon points="80,905 180,935 120,990" fill="#ececea"/>
    <polyline points="0,920 80,905 180,935 300,965 420,980 480,1018" fill="none" stroke="#acd136" stroke-width="6"/>
  </svg>
  <div class="headline headline--dark" style="left:45px;top:45px">
    <span>FAHRANGST</span><span>ERFOLGREICH</span><span>ÜBERWINDEN!</span>
  </div>
  <h2 class="section-title" style="left:95px;top:335px;font-size:27px">3 Schritte zur Lösung:</h2>
  <div class="steps">
    <div class="step" style="font-size:16px"><span class="num">1</span>Erstge-<br>spräch<br>verein-<br>baren</div>
    <div class="step" style="font-size:10px"><span class="num">2</span>Analyse<br>Ihrer<br>individuellen<br>Situation<br>und<br>Zielsetzung</div>
    <div class="step" style="font-size:11px"><span class="num">3</span>Individuelles<br>Coaching<br>und<br>Training</div>
  </div>
  <h2 class="section-title" style="left:45px;top:540px;font-size:24px">Advantages in the work with me:</h2>
  <ul class="checks">
    <li><svg width="20" height="20" viewBox="0 0 20 20"><circle cx="10" cy="10" r="10" fill="#acd136"/><path d="M5 10.5l3.2 3L15 6.5" fill="none" stroke="#fff" stroke-width="2.4"/></svg>Über 10 Jahre Erfahrung als <span class="green">Trainerin und Coach</span> im Bereich <span class="green">Fahrsicherheit</span></li>
    <li><svg width="20" height="20" viewBox="0 0 20 20"><circle cx="10" cy="10" r="10" fill="#acd136"/><path d="M5 10.5l3.2 3L15 6.5" fill="none" stroke="#fff" stroke-width="2.4"/></svg>Als <span class="green">psychotherapeutische Heilpraktikerin</span> bin ich <span class="green">auf Angststörungen und Panikattacken spezialisiert</span></li>
    <li><svg width="20" height="20" viewBox="0 0 20 20"><circle cx="10" cy="10" r="10" fill="#acd136"/><path d="M5 10.5l3.2 3L15 6.5" fill="none" stroke="#fff" stroke-width="2.4"/></svg><span class="green">100 % auf Sie zugeschnitten:</span> ich hole Sie genau dort ab, wo Sie jetzt stehen und unterstütze Sie <span class="green">in Ihrem Prozess individuell und zielführend.</span></li>
    <li><svg width="20" height="20" viewBox="0 0 20 20"><circle cx="10" cy="10" r="10" fill="#acd136"/><path d="M5 10.5l3.2 3L15 6.5" fill="none" stroke="#fff" stroke-width="2.4"/></svg><span class="green">Termine</span> sind auch <span class="green">abends und am Wochenende möglich</span></li>
    <li><svg width="20" height="20" viewBox="0 0 20 20"><circle cx="10" cy="10" r="10" fill="#acd136"/><path d="M5 10.5l3.2 3L15 6.5" fill="none" stroke="#fff" stroke-width="2.4"/></svg>Wenn es Ihnen nicht möglich ist, in meine Praxis nach Lindenfeld Süd zu kommen: <span class="green">Mit der mobilen Praxis komme ich auch zu Ihnen</span></li>
  </ul>
  <div class="coach-photo" role="img" aria-label="Porträtfoto der Trainerin in weißer Bluse"></div>
  <p class="contact-name">Karin Feldhaus</p>
  <p class="contact-more">Weitere Informationen finden Sie auf:</p>
  <p class="contact-web">
    <svg width="16" height="16" viewBox="0 0 16 16" aria-hidden="true"><g fill="none" stroke="#acd136" stroke-width="1.3"><circle cx="8" cy="8" r="7"/><ellipse cx="8" cy="8" rx="3" ry="7"/><path d="M1 8h14M2.5 4.5h11M2.5 11.5h11"/></g></svg>
    www.fahrsicher-coaching-beispiel.de
  </p>
  <p class="call-label">Oder rufen Sie mich einfach an:</p>
  <p class="call-number">
    <svg width="24" height="24" viewBox="0 0 24 24" aria-hidden="true"><rect width="24" height="24" rx="3" fill="#acd136"/><path d="M8 5c-1 0-2 1-2 2 0 6 5 11 11 11 1 0 2-1 2-2l-3-2-2 1.5c-2-1-3.5-2.5-4.5-4.5L11 9 9 6z" fill="#fff"/></svg>
    0170 12 34 56 78
  </p>
</section>

</body>
</html>
```